BENEATH THE [HARBOR] OF A DAWN, Mend your road

We are looking for a cover refresh of an existing bestselling book that is going into 3rd edition print this year.
The book is an inspirational as well as educational book that has become recognized as one of the most comprehensive, actionable, personal and financial planning resources available today for families, individuals and business owners alike.
Comprised of three true stories of loss, learning to live and love again and a 30 page checklist at the back of the book it contains tips and strategies for everyone to help them to get their personal and financial lives in order while they can.
The cover must have the following:
1. Appeal to a broad audience/both personal and corporate
2. Include Mara Quellton Bestselling Author
3. Include introduction of a new Afterword
4. 3rd Edition
5. Colors to remain the same – red, black and white
6. The title must remain in caps and the word [HARBOR] must have the brackets around it
We have also added a current copy of the second edition to help you. For your information our website is www.thequelltonhouse.example
Reason: We have narrowed it down to our top 3 designs. We are submitting the covers to our community for them to pick the top cover. Good luck to everyone

```html
<!DOCTYPE html>
<html lang="en">
<head>
<meta charset="utf-8">
<title>Beneath the [Harbor] of a Dawn — Mara Quellton</title>
<link rel="stylesheet" href="https://fonts.googleapis.com/css2?family=Oswald:wght@500;600;700&family=Anton&family=Pinyon+Script&display=swap">
<style>
  :root {
    --white: #ffffff;
    --black: #0b0a0a;
    --red: #d5161c;
    --red-deep: #9c1014;
    --wine: #3d0a0c;
    --slate: #6b6668;
    --slate-dark: #2f2b2c;
  }
  html, body {
    margin: 0;
    padding: 0;
    width: 851px;
    height: 1200px;
    overflow: hidden;
    background: var(--black);
  }
  h1, p { margin: 0; padding: 0; font-weight: inherit; font-size: inherit; }
  .cover {
    position: relative;
    width: 851px;
    height: 1200px;
    overflow: hidden;
    font-family: 'Oswald', sans-serif;
    color: var(--white);
  }
  .cover-art {
    position: absolute;
    inset: 0;
    background:
      radial-gradient(ellipse 60% 45% at 30% 28%, rgba(150,145,146,0.55), rgba(0,0,0,0) 70%),
      linear-gradient(180deg,
        var(--slate) 0%,
        #4f4a4b 28%,
        var(--slate-dark) 46%,
        #5a1518 60%,
        var(--red-deep) 72%,
        #6e0d10 86%,
        var(--wine) 100%);
  }
  .title-band {
    position: absolute;
    left: 0;
    top: 420px;
    width: 803px;
    height: 162px;
    background: var(--red);
    box-shadow: 0 4px 14px rgba(0,0,0,0.35);
  }
  .title-lead {
    position: absolute;
    left: 30px;
    font-weight: 700;
    font-size: 44px;
    line-height: 1;
    letter-spacing: 0.5px;
    color: var(--white);
    white-space: nowrap;
  }
  .title-lead--top { top: 440px; }
  .title-lead--bottom { top: 508px; }
  .title-key {
    position: absolute;
    left: 296px;
    top: 456px;
    font-family: 'Anton', sans-serif;
    font-size: 104px;
    line-height: 1.1;
    letter-spacing: 2px;
    color: var(--white);
    white-space: nowrap;
  }
  .title-key .bracket { color: var(--black); }
  .title-key .accent { color: var(--red-deep); }
  .tagline {
    position: absolute;
    left: 100px;
    width: 851px;
    top: 660px;
    text-align: center;
    font-family: 'Pinyon Script', cursive;
    font-size: 62px;
    line-height: 1.2;
    color: var(--white);
  }
  .author {
    position: absolute;
    left: 0;
    width: 851px;
    text-align: center;
    color: var(--white);
    line-height: 1.2;
  }
  .author-label {
    top: 1024px;
    font-weight: 600;
    font-size: 34px;
    letter-spacing: 0.5px;
  }
  .author-name {
    top: 1076px;
    font-weight: 600;
    font-size: 42px;
    letter-spacing: 1px;
  }
  .edition-strip {
    position: absolute;
    left: 0;
    bottom: 0;
    width: 851px;
    height: 50px;
    background: var(--black);
  }
  .edition-note {
    position: absolute;
    left: 0;
    top: 0;
    width: 851px;
    height: 50px;
    text-align: center;
    font-weight: 500;
    font-size: 26px;
    line-height: 50px;
    color: var(--red);
    white-space: nowrap;
  }
</style>
</head>
<body>
  <main class="cover">
    <div class="cover-art" role="img" aria-label="Close-up of a fountain pen nib resting on a page of handwritten script, tinted grey fading into deep red"></div>

    <div class="title-band"></div>
    <h1 class="title">
      <span class="title-lead title-lead--top">BENEATH THE</span>
      <span class="title-key"><span class="bracket">[</span>HAR<span class="accent">B</span>OR<span class="bracket">]</span></span>
      <span class="title-lead title-lead--bottom">OF A DAWN</span>
    </h1>

    <p class="tagline">Mend your road</p>

    <p class="author author-label">BESTSELLING AUTHOR</p>
    <p class="author author-name">MARA QUELLTON</p>

    <div class="edition-strip">
      <p class="edition-note">3rd EDITION - NEW AFTERWORD</p>
    </div>
  </main>
</body>
</html>
```